Software Platform/Architecture Drawing for website

We need a drawing of a software platform/application.

We are looking for someone to take these abstract concepts and put them into a concrete illustration style. Use the image as baseline description of the framework, not as a template.
See image attached.

The drawing should show the connections between the platform sections, and show that the platform is secure. Platform components can be presented with words or symbols.

There are 2 examples attached to show what kind of graphic we are looking for. Please do not re-create the provided platform drawing in the same concept. We are looking for something more creative to present to our clients.

Thank you.

Healthcare

• the components (not lanes) shown in the KT Platform.pdf design file.
• Please do not follow the same 4-lane concept shown in the attached example. This is an example to show the relationship between the lanes and components. The outside design should not follow the same layout.

```html
<!DOCTYPE html>
<html lang="en">
<head>
<meta charset="utf-8">
<title>KT Platform</title>
<link href="https://fonts.googleapis.com/css2?family=Arimo:wght@400;700&display=swap" rel="stylesheet">
<style>
  :root {
    --blue: #3b6db4;
    --blue-line: #4a72b8;
    --box-line: #6d8dc4;
    --peach: #fbe3d6;
    --halo: #f4f4f4;
    --secure-bg: #ebebeb;
    --green: #1fbf4a;
    --green-dark: #109a37;
    --text: #444444;
    --title: #555555;
    --person: #dbe4f1;
    --white: #ffffff;
  }
  html, body {
    margin: 0;
    padding: 0;
    width: 1200px;
    height: 750px;
    overflow: hidden;
    background: var(--white);
  }
  .canvas {
    display: block;
    width: 1200px;
    height: 750px;
    font-family: "Arimo", Arial, sans-serif;
  }
  .title { font-size: 22px; font-weight: 700; fill: var(--title); }
  .label { font-size: 11px; font-weight: 700; fill: var(--text); }
  .label-lg { font-size: 14px; font-weight: 700; fill: var(--text); }
  .ring-text { font-size: 15px; font-weight: 700; fill: var(--text); }
  .heading { font-size: 15px; font-weight: 700; fill: var(--text); font-variant: small-caps; letter-spacing: 0.3px; }
  .item { font-size: 11px; font-weight: 700; fill: var(--text); }
  .platform-frame { fill: none; stroke: var(--blue-line); stroke-width: 2.5; }
  .core-frame { fill: none; stroke: var(--blue-line); stroke-width: 2.5; stroke-dasharray: 6 5; }
  .halo { fill: var(--halo); }
  .ring { fill: var(--white); stroke: var(--blue); }
  .panel { fill: var(--peach); stroke: var(--box-line); stroke-width: 2; }
  .flow { fill: var(--blue); }
  .icon { fill: none; stroke: var(--blue); stroke-width: 1.8; stroke-linejoin: round; stroke-linecap: round; }
  .icon-fill { fill: var(--blue); }
  .icon-white { fill: var(--white); stroke: var(--blue); stroke-width: 1.8; }
  .person { fill: var(--person); }
  .secure-badge { fill: var(--secure-bg); stroke: var(--green); stroke-width: 3; stroke-dasharray: 5 5; }
  .lock-body { fill: var(--green); stroke: var(--green-dark); stroke-width: 1.5; }
  .lock-shackle { fill: none; stroke: var(--green-dark); stroke-width: 5; }
</style>
</head>
<body>
<svg class="canvas" viewBox="0 0 1280 800" xmlns="http://www.w3.org/2000/svg">
  <text class="title" x="638" y="67" text-anchor="middle">KT Platform</text>

  <rect class="platform-frame" x="173" y="103" width="931" height="500"/>

  <!-- patient interactions -->
  <g class="patient-interactions">
    <circle class="halo" cx="325" cy="315" r="150"/>
    <circle class="ring" cx="318" cy="316" r="56" stroke-width="12"/>
    <text class="ring-text" x="318" y="308" text-anchor="middle">Patient</text>
    <text class="ring-text" x="318" y="325" text-anchor="middle">Interactions</text>

    <g class="sms">
      <path class="icon" d="M260 193 h46 a3 3 0 0 1 3 3 v21 a3 3 0 0 1 -3 3 h-28 l-8 7 v-7 h-10 a3 3 0 0 1 -3 -3 v-21 a3 3 0 0 1 3 -3 z"/>
      <path class="icon" d="M268 202 h30 M268 207 h30 M268 212 h22"/>
      <text class="label" x="283" y="242" text-anchor="middle">SMS</text>
    </g>
    <g class="apps">
      <rect class="icon-white" x="347" y="178" width="31" height="50" rx="3"/>
      <rect class="icon-fill" x="351" y="184" width="23" height="34"/>
      <circle class="icon-fill" cx="362.5" cy="222.5" r="2"/>
      <text class="label" x="363" y="242" text-anchor="middle">APPS</text>
    </g>
    <g class="home-devices">
      <path class="icon" d="M200 280 a10 10 0 0 1 3 -18 a13 13 0 0 1 24 -8 a11 11 0 0 1 20 10 a8 8 0 0 1 2 16 z"/>
      <path class="icon" d="M213 270 l12 -10 l12 10 M216 268 v12 h18 v-12"/>
      <rect class="icon-fill" x="222" y="272" width="6" height="8"/>
      <text class="label" x="200" y="296">Home</text>
      <text class="label" x="200" y="308">Devices</text>
    </g>
    <g class="web">
      <circle class="icon" cx="233" cy="364" r="17"/>
      <path class="icon" d="M216 364 h34 M233 347 v34 M219 355 h28 M219 373 h28"/>
      <ellipse class="icon" cx="233" cy="364" rx="8" ry="17"/>
      <text class="label" x="233" y="398" text-anchor="middle">Web</text>
    </g>
    <g class="wearable">
      <path class="icon-white" d="M281 388 h87 l-4 20 h-79 z"/>
      <rect class="icon-fill" x="312" y="390" width="26" height="16"/>
      <path class="icon" d="M289 398 h0.1 M293 398 h0.1 M297 398 h0.1"/>
      <text class="label" x="318" y="427" text-anchor="middle">Wearable</text>
      <text class="label" x="318" y="439" text-anchor="middle">Devices</text>
    </g>
  </g>

  <!-- flows -->
  <polygon class="flow" points="100,304 145,304 145,295 163,310 145,325 145,316 100,316"/>
  <polygon class="flow" points="164,343 120,343 120,334 102,349 120,364 120,355 164,355"/>
  <polygon class="flow" points="393,287 440,287 440,278 458,293 440,308 440,299 393,299"/>
  <polygon class="flow" points="459,327 413,327 413,318 395,333 413,348 413,339 459,339"/>
  <polygon class="flow" points="862,304 903,304 903,295 921,310 903,325 903,316 862,316"/>
  <polygon class="flow" points="1110,288 1155,288 1155,279 1173,294 1155,309 1155,300 1110,300"/>
  <polygon class="flow" points="1175,327 1130,327 1130,318 1112,333 1130,348 1130,339 1175,339"/>

  <!-- core -->
  <rect class="core-frame" x="431" y="128" width="454" height="375"/>

  <g class="services">
    <rect class="panel" x="480" y="159" width="157" height="295"/>
    <text class="heading" x="507" y="200">Services</text>
    <text class="item" x="507" y="249">Logic</text>
    <path class="icon" d="M575 243 h6 a4 4 0 1 1 7 0 h6 v7 a4 4 0 1 0 0 7 v7 h-7 a4 4 0 1 0 -6 0 h-6 v-7 a4 4 0 1 1 0 -7 z"/>
    <text class="item" x="507" y="305">DB</text>
    <ellipse class="icon" cx="589" cy="291" rx="13" ry="5"/>
    <path class="icon" d="M576 291 v24 a13 5 0 0 0 26 0 v-24 M576 299 a13 5 0 0 0 26 0 M576 307 a13 5 0 0 0 26 0"/>
    <text class="item" x="505" y="358">Identity &amp;</text>
    <text class="item" x="505" y="370">Access</text>
    <text class="item" x="505" y="383">Control</text>
    <path class="icon" d="M582 358 v-7 a7 7 0 0 1 14 0 v7"/>
    <rect class="icon" x="577" y="358" width="24" height="20" rx="2"/>
    <circle class="icon" cx="589" cy="369" r="1.5"/>
  </g>

  <g class="external-connections">
    <rect class="panel" x="652" y="159" width="200" height="295"/>
    <text class="heading" x="661" y="200">External Connections</text>
    <rect class="icon" x="684" y="226" width="29" height="35" rx="1"/>
    <rect class="icon-fill" x="693" y="222" width="11" height="6" rx="1"/>
    <path class="icon" d="M691 234 v8 M687 238 h8 M699 236 h9 M699 241 h9 M689 248 h19 M689 253 h19"/>
    <text class="item" x="747" y="247">EHR</text>
    <rect class="icon" x="685" y="288" width="35" height="22"/>
    <path class="icon-fill" d="M685 288 h35 l-17.5 14 z"/>
    <text class="item" x="747" y="301">Email</text>
    <rect class="icon" x="684" y="340" width="8" height="7"/>
    <rect class="icon" x="717" y="338" width="8" height="7"/>
    <rect class="icon" x="686" y="364" width="8" height="7"/>
    <rect class="icon" x="701" y="368" width="8" height="7"/>
    <rect class="icon-fill" x="697" y="350" width="14" height="9"/>
    <path class="icon" d="M688 347 v4 h9 M711 354 h10 v-9 M704 359 v9 M697 356 h-7 v8"/>
    <text class="item" x="747" y="355">Hub Systems</text>
    <path class="icon-white" d="M680 399 h22 v13 h-14 l-5 5 v-5 h-3 z"/>
    <path class="icon-fill" d="M706 404 h20 v12 h-4 v5 l-5 -5 h-11 z"/>
    <text class="item" x="747" y="411">Social Media</text>
  </g>

  <!-- output -->
  <g class="output">
    <ellipse class="halo" cx="980" cy="318" rx="125" ry="155"/>
    <circle class="ring" cx="981" cy="306" r="48" stroke-width="10"/>
    <text class="ring-text" x="981" y="311" text-anchor="middle">Output</text>

    <rect class="icon-white" x="944" y="187" width="73" height="42"/>
    <path class="icon" d="M949 194 h63"/>
    <rect class="icon" x="950" y="202" width="28" height="13"/>
    <path class="icon" d="M984 203 h27 M984 209 h27 M984 215 h27 M950 221 h61"/>
    <text class="label" x="981" y="245" text-anchor="middle">Web Portal</text>

    <rect class="icon-white" x="916" y="366" width="66" height="38"/>
    <path class="icon" d="M921 372 h56"/>
    <rect class="icon" x="921" y="377" width="15" height="22"/>
    <rect class="icon" x="941" y="377" width="35" height="5"/>
    <rect class="icon" x="941" y="386" width="15" height="5"/>
    <rect class="icon" x="960" y="386" width="16" height="5"/>
    <rect class="icon" x="941" y="394" width="15" height="5"/>
    <rect class="icon" x="960" y="394" width="16" height="5"/>
    <text class="label" x="950" y="421" text-anchor="middle">User Portal</text>

    <rect class="icon-white" x="1010" y="364" width="40" height="40"/>
    <rect class="icon" x="1016" y="370" width="28" height="28"/>
    <path class="icon" d="M1022 377 h16 M1022 383 h16 M1022 389 h16"/>
    <text class="label" x="1030" y="420" text-anchor="middle">Admin Portal</text>
  </g>

  <!-- people -->
  <g class="customer">
    <rect class="person" role="img" aria-label="Customer or patient figure" x="41" y="302" width="52" height="62" rx="14"/>
    <text class="label-lg" x="38" y="391">Customer/</text>
    <text class="label-lg" x="38" y="408">Patient</text>
  </g>
  <g class="administrator">
    <rect class="person" role="img" aria-label="Administrator figure" x="1180" y="270" width="52" height="68" rx="14"/>
    <text class="label-lg" x="1195" y="358" text-anchor="middle">Administrator</text>
  </g>

  <!-- secure badge -->
  <g class="secure-platform">
    <circle class="secure-badge" cx="526" cy="605" r="77"/>
    <path class="lock-shackle" d="M513 582 v-8 a13 13 0 0 1 26 0 v8"/>
    <rect class="lock-body" x="505" y="580" width="43" height="32" rx="2"/>
    <circle cx="526" cy="597" r="3.5" fill="none" stroke="#ffffff" stroke-width="2"/>
    <text class="label-lg" x="526" y="631" text-anchor="middle">Secure Platform</text>
  </g>
</svg>
</body>
</html>
```